Food humor T-shirt and apparel company needs a Cartwell site designed. We have logo files to help.

We are an apparel company based in Chicago by two cooking and food humor enthusiasts. We are looking for a redesign of our Cartwell site. Our products are humorous quotes and pictures on shirts, sweaters and other apparel. The tagline for the company is - Find Your Yum. Wear Your Food. We want to see designs that incorporate our logo, brand color of royal purple, signify fun business casual clothing with amusing tags or images of trendy or esoteric food trends. The design should communicate excellence in taste but with maybe a satirical almost corporate type spin.
Target Market(s)
Hip, millennial foodies and cooks that love to try new foods, have great taste, and love to experiment in the restaurant or the kitchen.
Industry/Entity Type
Cooking
Look and feel

```html
<!DOCTYPE html>
<html lang="en">
<head>
<meta charset="utf-8">
<title>Snackory — Find Your Yum. Wear Your Food</title>
<link href="https://fonts.googleapis.com/css2?family=Mulish:wght@400;600;700;800&family=Montserrat:wght@600;700&display=swap" rel="stylesheet">
<style>
:root{
  --bg:#ececec;
  --white:#ffffff;
  --purple:#6b3fa0;
  --purple-soft:#9a7cc2;
  --blue:#0d4fa0;
  --footer:#2f77b7;
  --ink:#1d1d1d;
  --muted:#8a8a8a;
  --deco-purple:rgba(154,124,194,.28);
  --deco-blue:rgba(110,160,210,.3);
}
*{box-sizing:border-box;margin:0;padding:0}
html,body{width:964px;height:1200px;overflow:hidden}
body{background:var(--bg);font-family:'Mulish',sans-serif;color:var(--ink);position:relative}
.abs{position:absolute}
.brand{left:28px;top:15px;width:55px;height:40px;background:var(--white);display:flex;align-items:center;justify-content:center;font-weight:800;font-size:9px;color:var(--purple)}
.nav{left:263px;top:15px;width:439px;height:40px;background:var(--white)}
.nav a{position:absolute;top:16px;transform:translateX(-50%);font-family:'Montserrat',sans-serif;font-weight:700;font-size:8px;letter-spacing:1px;color:var(--purple);text-decoration:none;white-space:nowrap}
.nav .divider{position:absolute;top:7px;width:1px;height:25px;background:#9a9a9a}
.nav .active-bar{position:absolute;left:22px;top:38px;width:35px;height:2px;background:var(--purple)}
.btn-account{left:738px;top:25px;width:95px;height:20px;border:1.5px solid var(--blue);border-radius:7px;font-family:'Montserrat',sans-serif;font-weight:700;font-size:6.5px;color:var(--blue);display:flex;align-items:center;justify-content:center;letter-spacing:.3px}
.login{left:851px;top:30px;font-size:8px;color:var(--purple);font-weight:600;letter-spacing:.3px}
.cart{left:912px;top:25px}
.hero-title{left:0;width:964px;top:82px;text-align:center;font-size:10px;color:var(--purple);font-weight:600;letter-spacing:.6px}
.hero-sub{left:0;width:964px;top:94px;text-align:center;font-size:5.3px;color:var(--purple-soft)}
.search{left:370px;top:112px;width:224px;height:20px;border:1.5px solid var(--purple);border-radius:5px;background:var(--white)}
.search span{position:absolute;left:11px;top:5px;font-size:7px;color:#aaa;letter-spacing:.3px}
.search svg{position:absolute;right:11px;top:4px}
.deco{border-radius:40%}
.deco.p{background:var(--deco-purple)}
.deco.b{background:var(--deco-blue)}
.card{width:186px;height:186px;background:var(--white)}
.product-name{font-size:7.5px;color:#333}
.product-price{font-size:7.5px;font-weight:700}
.blog-heading{left:0;width:964px;top:883px;text-align:center;font-family:'Montserrat',sans-serif;font-weight:700;font-size:10px;letter-spacing:7px;color:var(--purple)}
.post{width:168px;font-size:7px;line-height:12.4px}
.post h3{font-weight:800;font-size:7.8px;line-height:13px;color:var(--purple);text-transform:uppercase}
.post time{display:block;color:var(--blue);font-size:7.5px;margin-bottom:4px}
.post p{text-align:justify;color:#222}
.post .more{color:var(--blue);text-transform:uppercase;font-weight:600}
.news-title{left:0;width:964px;top:1054px;text-align:center;font-family:'Montserrat',sans-serif;font-weight:700;font-size:10.5px;letter-spacing:.4px}
.news-sub{left:0;width:964px;top:1069px;text-align:center;font-size:6.5px}
.email{left:403px;top:1087px;width:101px;height:17px;border:1px solid #333;background:var(--white);font-size:5.5px;color:#999;padding:5px 8px}
.subscribe{left:504px;top:1087px;width:57px;height:17px;background:var(--blue);color:var(--white);font-size:4.5px;font-weight:800;display:flex;align-items:center;justify-content:center}
.footer{left:0;top:1153px;width:964px;height:47px;background:var(--footer);color:var(--white)}
.footer .links{position:absolute;top:8px;left:0;width:964px;text-align:center;font-size:5.5px;font-weight:700}
.footer .links a{color:var(--white);text-decoration:none;margin:0 10px}
.footer .copy{position:absolute;top:32px;left:0;width:964px;text-align:center;font-size:5px}
</style>
</head>
<body>

<div class="abs brand">Snackory</div>

<nav class="abs nav">
  <a style="left:39px">HOME</a>
  <span class="divider" style="left:79px"></span>
  <a style="left:119px">SHOP</a>
  <span class="divider" style="left:158px"></span>
  <a style="left:208px">ABOUT US</a>
  <span class="divider" style="left:259px"></span>
  <a style="left:310px">PRODUCTS</a>
  <span class="divider" style="left:362px"></span>
  <a style="left:401px">BLOG</a>
  <span class="active-bar"></span>
</nav>

<div class="abs btn-account">CREATE ACCOUNT</div>
<div class="abs login">LOG IN</div>
<svg class="abs cart" width="18" height="18" viewBox="0 0 18 18" fill="none" stroke="#6b3fa0" stroke-width="1.1">
  <path d="M1 2h2.5l2 9h9l1.5-6H5"/><circle cx="7" cy="14.5" r="1.2"/><circle cx="13.5" cy="14.5" r="1.2"/>
</svg>

<div class="abs hero-title">Find Your Yum. Wear Your Food</div>
<div class="abs hero-sub">Apparel and kitchenware to inspire while you cook up and eat up!</div>
<div class="abs search"><span>SEARCH</span>
  <svg width="11" height="11" viewBox="0 0 11 11" fill="none" stroke="#6b3fa0" stroke-width="1.2"><circle cx="4.5" cy="4.5" r="3.5"/><path d="M7 7l3 3"/></svg>
</div>

<div class="abs deco b" style="left:240px;top:121px;width:48px;height:41px" role="img" aria-label="Outline burger doodle"></div>
<div class="abs deco p" style="left:99px;top:285px;width:69px;height:80px" role="img" aria-label="Outline pizza slice doodle"></div>
<div class="abs deco p" style="left:837px;top:323px;width:50px;height:54px" role="img" aria-label="Outline fries box doodle"></div>
<div class="abs deco b" style="left:864px;top:671px;width:77px;height:76px" role="img" aria-label="Outline pizza slice doodle"></div>
<div class="abs deco p" style="left:152px;top:1055px;width:39px;height:44px" role="img" aria-label="Outline fries box doodle"></div>

<!-- Row 1 -->
<div class="abs card" style="left:168px;top:162px;background:radial-gradient(ellipse 32% 36% at 48% 45%,#f15a0e 90%,#fff 100%)" role="img" aria-label="Orange T-shirt product photo"></div>
<div class="abs product-name" style="left:168px;top:356px">Orange T-shirt</div>
<div class="abs product-price" style="left:168px;top:368px">30$</div>

<div class="abs card" style="left:389px;top:162px;background:radial-gradient(ellipse 30% 38% at 53% 50%,#9b1020 90%,#fff 100%)" role="img" aria-label="Red T-shirt product photo"></div>
<div class="abs product-name" style="left:389px;top:357px">Red T-shirt limited edition</div>
<div class="abs product-price" style="left:389px;top:369px">35$</div>

<div class="abs card" style="left:610px;top:162px;background:radial-gradient(ellipse 32% 40% at 48% 50%,#eeb130 90%,#fff 100%)" role="img" aria-label="Yellow printed T-shirt product photo"></div>
<div class="abs product-name" style="left:610px;top:357px">Yellow T-shirt with text</div>
<div class="abs product-price" style="left:610px;top:369px">31$</div>

<!-- Row 2 -->
<div class="abs card" style="left:168px;top:394px;background:radial-gradient(ellipse 31% 40% at 50% 52%,#1d2747 90%,#fff 100%)" role="img" aria-label="Navy T-shirt product photo"></div>
<div class="abs product-name" style="left:168px;top:585px">Blue T-shirt Pizza edition</div>
<div class="abs product-price" style="left:168px;top:597px">40$</div>

<div class="abs card" style="left:389px;top:394px;background:radial-gradient(ellipse 32% 36% at 52% 45%,#f15a0e 90%,#fff 100%)" role="img" aria-label="Orange T-shirt product photo"></div>
<div class="abs product-name" style="left:389px;top:584px">Orange T-shirt</div>
<div class="abs product-price" style="left:389px;top:596px">21$</div>

<div class="abs card" style="left:610px;top:394px;background:radial-gradient(ellipse 30% 38% at 53% 50%,#9b1020 90%,#fff 100%)" role="img" aria-label="Red T-shirt product photo"></div>
<div class="abs product-name" style="left:610px;top:584px">Red T-shirt unlimited edition</div>
<div class="abs product-price" style="left:610px;top:596px">20$</div>

<div class="abs deco b" style="left:341px;top:601px;width:46px;height:54px" role="img" aria-label="Outline taco doodle"></div>

<!-- Row 3 -->
<div class="abs card" style="left:168px;top:625px;background:radial-gradient(ellipse 32% 36% at 48% 45%,#f15a0e 90%,#fff 100%)" role="img" aria-label="Orange T-shirt product photo"></div>
<div class="abs product-name" style="left:168px;top:819px">Orange T-shirt</div>
<div class="abs product-price" style="left:168px;top:831px">30$</div>

<div class="abs card" style="left:389px;top:625px;background:radial-gradient(ellipse 30% 38% at 53% 50%,#9b1020 90%,#fff 100%)" role="img" aria-label="Red T-shirt product photo"></div>
<div class="abs product-name" style="left:389px;top:820px">Red T-shirt limited edition</div>
<div class="abs product-price" style="left:389px;top:832px">35$</div>

<div class="abs card" style="left:610px;top:625px;background:radial-gradient(ellipse 32% 40% at 48% 50%,#eeb130 90%,#fff 100%)" role="img" aria-label="Yellow printed T-shirt product photo"></div>
<div class="abs product-name" style="left:610px;top:820px">Yellow T-shirt with text</div>
<div class="abs product-price" style="left:610px;top:832px">31$</div>

<h2 class="abs blog-heading">BLOG</h2>

<article class="abs post" style="left:168px;top:920px">
  <h3>I'm parched, let's drink: Vesper Bar, North Center, Chicago</h3>
  <time>April 14, 2019</time>
  <p>Show me a bartender that doesn't taste, and I show you cocktail that may not be worth your sips or your silver. The three brothers of the sultry, slinky Vesper... <span class="more">Learn more</span></p>
</article>

<article class="abs post" style="left:421px;top:920px">
  <h3>Salted caramel apple pie minis</h3>
  <time>April 14, 2019</time>
  <p style="text-align:left">Dearly Beloved, we are gathered here today to celebrate the union of salted caramel sauce and warm spiced apples. I present to you a recipe for a dessert marriage made in... <span class="more">Learn more</span></p>
</article>

<article class="abs post" style="left:632px;top:920px">
  <h3>Just landed, let's eat: Lumi Cafe, Chinatown, Chicago</h3>
  <time>April 14, 2019</time>
  <p>Hey, Boy. Take me to Lumi Cafe after midnight on that BYOB tip. You bring a DOCG Pinot Grigio and I'll raise you a bottle of the DOCG Chianti that I stowed... <span class="more">Learn more</span></p>
</article>

<h2 class="abs news-title">SUBSCRIBE TO OUR NEWSLETTER</h2>
<p class="abs news-sub">Discover Snackory's latest musings: favorite recipes, travel spots, and food haunts.</p>
<div class="abs email">Email Address</div>
<div class="abs subscribe">SUBSCRIBE</div>

<footer class="abs footer">
  <div class="links"><a>Contact</a><a>Privacy Policy</a><a>Return Policy</a></div>
  <div class="copy">© 2019, Snackory. Powered by Cartwell</div>
</footer>

</body>
</html>
```